Up and coming Australian Systems Integrator needs a proposal template refresh

We need to update our proposal template and are looking for a fresh, modern, simple and elegant proposal template. We'd like to keep our existing logos if possible.
NovaLink is a privately owned company operating since 2006. Offices and technical staff located in Quarry Bay and Bendigo
Sustained, profitable growth year on year
Velnet strategic partner
Velnet Advanced Enterprise Network Architecture Specialisation
Velnet Advanced Security Architecture Specialisation
Velnet Advanced Collaboration Architecture Specialisation
Velnet Advanced Unified Computing Technology Specialisation
Velnet Advanced Data Centre Architecture Specialisation (in progress)
Velnet Gold Partner – Expect 2H2018
As well as being a Velnet partner we have a well established stable of other vendors such as Brakwell, Tavrimo, Harbourtone, DPQ, Moltrane Dialogic, Zell, SkyTrover, VoLERNA Drift)
We are a top two provider of Velnet product/services in the Victorian healthcare sector.
Updates
Please feel free to use different colors and fonts as we feel the existing ones look dated.

```html
<!DOCTYPE html>
<html lang="en">
<head>
<meta charset="utf-8">
<title>NovaLink Proposal Template</title>
<link rel="stylesheet" href="https://fonts.googleapis.com/css2?family=Montserrat:wght@400;500;600;700&family=Open+Sans:wght@400;600;700&display=swap">
<style>
:root{
  --navy:#1d3a78;
  --navy-deep:#1a3573;
  --ink:#333a44;
  --text:#5a5f66;
  --blue:#1f6fd1;
  --bar:#4a8fdb;
  --slate:#3b3d41;
  --grey-band:#6b6e73;
  --table-head:#1d3a78;
  --table-row:#dce8f7;
  --rule:#9fb6d8;
  --orange:#f07f2b;
  --yellow:#f6b81a;
  --ring:#a6a6a6;
  --stage:#a8a9ab;
}
*{margin:0;padding:0;box-sizing:border-box}
html,body{width:1200px;height:1200px;overflow:hidden}
body{background:var(--stage);font-family:"Open Sans",sans-serif;position:relative}
.page{position:absolute;width:265px;height:358px;background:#fff;box-shadow:2px 3px 6px rgba(0,0,0,.35);overflow:hidden}
.c1{left:33px}.c2{left:324px}.c3{left:615px}.c4{left:907px}
.r1{top:35px}.r2{top:421px}.r3{top:810px}

.head-bar{position:absolute;left:0;top:24px;width:20px;height:7px;background:var(--navy)}
.head-title{position:absolute;left:27px;top:21px;font-family:"Montserrat",sans-serif;font-size:9px;font-weight:400;color:var(--navy);letter-spacing:.2px;text-transform:uppercase}
.foot-rule{position:absolute;left:26px;right:26px;top:341px;height:1px;background:var(--rule)}
.foot-logo{position:absolute;left:26px;top:335px;display:flex;align-items:center;gap:2px;font-family:"Montserrat",sans-serif;font-size:4.6px;font-weight:600;color:var(--navy);background:#fff;padding-right:2px}
.foot-logo i{display:block;width:4px;height:4px;border-radius:50%;background:var(--navy)}
.foot-num{position:absolute;right:26px;top:338px;width:28px;height:4px;background:var(--navy);color:#fff;font-size:3px;text-align:center;line-height:4px}

.p{position:absolute;font-size:4.1px;line-height:7.4px;color:var(--text)}
.p + .p{}
.h{position:absolute;font-family:"Montserrat",sans-serif;font-weight:500;color:var(--ink)}
.h2{font-size:7.2px}
.em{font-style:italic;color:#7b7f86}
.link{color:var(--blue)}
.lead{color:var(--blue);font-weight:600}

/* cover */
.cover-logo{position:absolute;left:30px;top:80px;width:140px;text-align:center;font-family:"Montserrat",sans-serif;color:var(--navy)}
.cover-logo .name{display:flex;align-items:center;justify-content:center;gap:4px;font-size:13px;font-weight:600;letter-spacing:1px}
.cover-logo .name i{display:block;width:9px;height:9px;border-radius:50%;background:var(--navy)}
.cover-logo .tag{font-size:3.3px;letter-spacing:.6px;margin-top:1px}
.cover-title{position:absolute;left:0;width:265px;top:300px;text-align:center;font-family:"Montserrat",sans-serif;font-weight:700;font-size:12.5px;line-height:15px;color:var(--navy)}
.cover-sub{position:absolute;left:0;width:265px;top:340px;text-align:center;font-size:8.2px;color:#8a8d92}
.cover-date{position:absolute;left:0;width:265px;top:363px}
.cover-date span{display:block;text-align:center;font-size:7px;font-weight:700;color:var(--navy)}

/* tables */
table{border-collapse:collapse;position:absolute}
.rev td,.rev th{border:1px solid #c5cdd8;height:11px;font-size:3.5px;font-weight:400;color:var(--blue);text-align:left;padding-left:2px}
.rev td:nth-child(2){background:#eef0f3}
.budget td{border:1px solid #b7c9e6;height:9px}
.budget tr.top td{background:var(--table-head);height:9px}
.budget tr:nth-child(even) td{background:var(--table-row)}
.budget.light td{border-color:#b7c9e6;background:#fff}
.budget.light tr:nth-child(odd) td{background:var(--table-row)}

/* toc */
.toc{position:absolute;left:30px;top:71px;width:210px;list-style:none}
.toc li{display:flex;align-items:baseline;font-size:4.1px;line-height:8.4px;color:var(--ink)}
.toc li .dots{flex:1;border-bottom:1px dotted #777;margin:0 4px;transform:translateY(-1px)}

/* vision banner */
.banner{position:absolute;left:27px;top:42px;width:210px;height:22px;background:var(--grey-band);display:flex;align-items:center}
.banner .icon{width:22px;height:22px;background:var(--blue);display:flex;align-items:center;justify-content:center}
.banner p{font-size:4.1px;line-height:5px;color:#fff;padding:0 8px}

/* bullets */
.bl{position:absolute;left:27px;width:210px;font-size:4.1px;line-height:7.4px;color:var(--blue)}
.bl b{color:var(--blue)}
.sq{color:var(--navy)}
.black{color:var(--text)}

/* photos */
.photo{position:absolute}

/* back cover */
.back{background:var(--navy-deep)}
.back-logo{position:absolute;left:0;width:265px;top:275px;text-align:center;font-family:"Montserrat",sans-serif;color:#fff}
.back-logo .name{display:flex;align-items:center;justify-content:center;gap:4px;font-size:11px;font-weight:600;letter-spacing:1px}
.back-logo .name i{display:block;width:8px;height:8px;border-radius:50%;background:#fff}
.back-logo .tag{font-size:3px;letter-spacing:.5px;margin-top:1px}
.contact{position:absolute;left:0;width:265px;top:327px;text-align:center;font-size:3.4px;color:#e6ecf7;line-height:6px}
.contact span{margin:0 4px}
.contact svg{vertical-align:-1px;margin-right:2px}
</style>
</head>
<body>

<!-- 1 Cover -->
<section class="page c1 r1">
  <svg width="265" height="358" viewBox="0 0 265 358" style="position:absolute;left:0;top:0">
    <path d="M168 0 H265 V355 C258 330 245 300 225 285 C185 262 120 262 0 272 V258 C90 240 160 215 175 150 C188 90 170 40 168 0 Z" fill="#b9bcc1"/>
    <path d="M158 0 H265 V330 C250 295 215 270 160 262 C95 254 40 258 0 263 V232 C70 215 140 180 158 120 C170 75 162 30 158 0 Z" fill="var(--navy)"/>
    <path d="M0 145 C60 150 110 175 130 225 C95 240 45 248 0 252 Z" fill="var(--slate)"/>
  </svg>
  <div class="cover-logo"><div class="name"><i></i>NOVALINK</div><div class="tag">NETWORK &amp; COMMUNICATIONS SOLUTIONS</div></div>
  <div class="cover-title">LOREM IPSUM IS SIMPLY<br>DUMMY HAS BEEN</div>
  <div class="cover-sub" style="top:342px">Lorem Ipsum Is Simply Dummy Has Been</div>
</section>
<div style="position:absolute;left:33px;top:397px;width:265px;text-align:center;font-size:0"></div>

<!-- 2 Revision page -->
<section class="page c2 r1">
  <table class="rev" style="left:37px;top:32px;width:193px">
    <tr><th style="width:28px">Version #</th><th style="width:80px">Purpose / Changes</th><th style="width:54px">Author</th><th>Date</th></tr>
    <tr><td></td><td></td><td></td><td></td></tr>
    <tr><td></td><td></td><td></td><td></td></tr>
    <tr><td></td><td></td><td></td><td></td></tr>
    <tr><td></td><td></td><td></td><td></td></tr>
    <tr><td></td><td></td><td></td><td></td></tr>
    <tr><td></td><td></td><td></td><td></td></tr>
  </table>
  <div class="p" style="left:54px;top:300px;width:190px;line-height:4.6px;font-size:3.4px;color:var(--blue)">Copyright © 2018 NovaLink Limited<br>All Rights Reserved</div>
  <div style="position:absolute;left:54px;top:313px;width:180px;height:1px;background:#c5cdd8"></div>
  <div class="p" style="left:54px;top:315px;width:190px;line-height:4.6px;font-size:3.4px;color:#666">No part of the contents of this document may be reproduced or distributed in any form or<br>by any means without the prior written permission of NovaLink Limited</div>
</section>

<!-- 3 Table of contents -->
<section class="page c3 r1">
  <div class="head-bar"></div><div class="head-title">Table of Contents</div>
  <div class="h" style="left:30px;top:56px;font-size:6.2px;font-weight:600">Contents</div>
  <ul class="toc">
    <li>Table of Contents<span class="dots"></span>01</li>
    <li>Executive Summary<span class="dots"></span>02</li>
    <li>Our Understanding of Your Needs<span class="dots"></span>02</li>
    <li>Our Recommendations<span class="dots"></span>03</li>
    <li>Our Approach<span class="dots"></span>05</li>
    <li>Budget and Timeframe<span class="dots"></span>07</li>
    <li>Appendix A: About Harlan Creek<span class="dots"></span>10</li>
    <li>Appendix B: Selected Client List<span class="dots"></span>10</li>
    <li>Appendix C: Our Capabilities<span class="dots"></span>11</li>
    <li>Appendix D: Our Process<span class="dots"></span>12</li>
  </ul>
  <div class="foot-rule"></div><div class="foot-logo"><i></i>NOVALINK</div><div class="foot-num">3</div>
</section>

<!-- 4 Budget -->
<section class="page c4 r1">
  <div class="head-bar"></div><div class="head-title">Budget and Timeframe</div>
  <div class="h h2" style="left:26px;top:41px">Implementation Estimate</div>
  <div class="p" style="left:26px;top:50px;width:215px">The bulk of the implementation costs will be defined by discovery. Based on similar CRM implementation projects, we feel expect that the CRM side will be somewhere between 200 and 300 hours, give or take. The wide swing in hours in phase one is related to the undefined nature of both the integration needs and our role in the integration project. Our focus in discovery (as mentioned above) will be to nail down those requirements and our role as it relates to what is needed to integrate the sites with the CRM.</div>
  <table class="budget" style="left:26px;top:101px;width:215px">
    <tr class="top"><td></td><td></td><td></td></tr>
    <tr><td></td><td></td><td></td></tr><tr><td></td><td></td><td></td></tr>
    <tr><td></td><td></td><td></td></tr><tr><td></td><td></td><td></td></tr>
    <tr><td></td><td></td><td></td></tr><tr><td></td><td></td><td></td></tr>
  </table>
  <table class="budget light" style="left:26px;top:190px;width:215px">
    <tr><td></td><td></td><td></td><td></td><td></td></tr><tr><td></td><td></td><td></td><td></td><td></td></tr>
    <tr><td></td><td></td><td></td><td></td><td></td></tr><tr><td></td><td></td><td></td><td></td><td></td></tr>
    <tr><td></td><td></td><td></td><td></td><td></td></tr><tr><td></td><td></td><td></td><td></td><td></td></tr>
    <tr><td></td><td></td><td></td><td></td><td></td></tr><tr><td></td><td></td><td></td><td></td><td></td></tr>
  </table>
  <div class="h h2" style="left:26px;top:269px">Implementation Estimate</div>
  <div class="p" style="left:26px;top:278px;width:215px">The bulk of the implementation costs will be defined by discovery. Based on similar CRM implementation projects, we feel expect that the CRM side will be somewhere between 200 and 300 hours, give or take. Our requirements and our role as it relates to what is needed to integrate the sites with the CRM.</div>
  <div class="foot-rule"></div><div class="foot-logo"><i></i>NOVALINK</div><div class="foot-num">5</div>
</section>

<!-- 5 Our Vision -->
<section class="page c1 r2">
  <div class="head-bar"></div><div class="head-title">Our Vision</div>
  <div class="banner"><div class="icon">
    <svg width="14" height="14" viewBox="0 0 14 14"><circle cx="7" cy="7" r="6" fill="none" stroke="#fff" stroke-width="1"/><circle cx="7" cy="7" r="3.5" fill="none" stroke="#fff" stroke-width="1"/><circle cx="7" cy="7" r="1.2" fill="#fff"/><path d="M7 7 L12 2" stroke="#fff" stroke-width="1"/></svg>
  </div><p>Tallyo's mission is to help and support the self-employed and small business owners with their administrative tasks so they can focus on what matters – their business.</p></div>
  <div class="p" style="left:27px;top:70px;width:210px">Administrative tasks are cumbersome, time-consuming and often prevent small owners from focusing their time and energy on their business and their customers. They can also be extremely stressful and nerve-wracking for those attempting these tasks for the first time.</div>
  <div class="p" style="left:27px;top:94px;width:210px;text-align:center">At Tallyo, we envisage accounting for the self-employed and small business owners as being <span class="link">automated and decentralized</span></div>
  <div class="p" style="left:27px;top:117px;width:210px">Accounting can and should be done automatically. By connecting to all sources of accounting data such as bank accounts, payment systems, e-commerce websites, and invoicing systems, Tallyo AI automatically completes these tasks, which would take hours to do manually. Bookings are created automatically and fully completed. Financial statements are available within a couple of clicks, and after analysing your data, Tallyo AI will offer you tips to improve your financial stability.</div>
  <div class="p" style="left:27px;top:157px;width:210px">What may seem like a pipedream to the millions of self-employed who struggle with their admin, is already a reality. Now is the time to join Tallyo on its mission to transform the world of bookkeeping through the power of AI</div>
  <div class="h" style="left:27px;top:180px;font-size:6.8px">The Tallyo model</div>
  <div class="p" style="left:27px;top:189px;width:210px">Tallyo is based on an innovative license model that uses Token-as-a-License (TaaL). The token represents lifelong software license for Tallyo solutions. The Pre-ICO token sales will enable Tallyo to complete its development of Tallyo AI to deliver fully automatic bookkeeping.</div>
  <div class="p" style="left:27px;top:213px;width:210px">The Pre-ICO token sale will also pave the way for a future Tallyo ICO. Tallyo will launch accounting on the blockchain and ensure your accounting data is comprehensive and private, but available everywhere within your preferred apps. It will empower you to manage your data as you see fit in a fully decentralized way.<br>Furthermore, a new range of business apps will connect to Tallyo to provide you<br><br>with leading edge business data access to ensure you have the best available data at your fingertips.</div>
  <div class="p" style="left:27px;top:270px;width:210px">Tallyo supports strong data ownership laws that truly protect individuals and ensure they have complete ownership of their data. Through decentralisation Tallyo helps to ensure you always have full ownership of your data to decide how it should be used.</div>
  <div class="p" style="left:27px;top:300px;width:210px">To find out more about the Tallyo AI project, and the Tallyo TaaL or if you are interested in purchasing Tallyo TaaL, please register with your email at <span class="link" style="text-decoration:underline">https://www.tallyo.io/en/ico</span> so we can notify you about our upcoming purchase periods.</div>
  <div class="foot-rule"></div><div class="foot-logo"><i></i>NOVALINK</div><div class="foot-num">5</div>
</section>

<!-- 6 Pre-ICO with donut -->
<section class="page c2 r2">
  <div class="head-bar"></div><div class="head-title">Headline Here</div>
  <div class="h h2" style="left:27px;top:46px">Pre-ICO Token sale</div>
  <div class="p" style="left:27px;top:55px;width:212px">To realize this innovative vision, Tallyo is launching a pre-ICO in form of a token sale on Brindle blockchain. 20,000,000 tokens are available to purchase for the price of CHF 0.10 each during a 30-day period to be announced. Tokens represent Tallyo lifelong software licenses and by purchasing enough tokens, holders gain access to Tallyo software. 15,000 tokens give access to Tallyo invoicing or accounting. 20,000 tokens give access to both Tallyo accounting and invoicing. Future customers will still have the opportunity to buy directly yearly or monthly subscriptions to have access to Tallyo.</div>
  <div class="h h2" style="left:27px;top:116px">Future plans</div>
  <div class="p" style="left:27px;top:125px;width:212px">A future ICO is planned between 18 and 24 months after the pre-ICO token sale. This offering will support the development of Tallyo into a fully decentralized, privacy-focused ecosystem of applications. The new model will reward each participant so that a new world with zero administrative tasks becomes reality.</div>
  <div style="position:absolute;left:0;width:265px;top:168px;text-align:center;font-family:'Montserrat',sans-serif;font-size:6.8px;line-height:8px;color:#222">USE OF FOUNDER SEED CAPITAL<br>$1.12M SINCE JAN 2014</div>
  <div style="position:absolute;left:0;width:265px;top:187px;text-align:center;font-size:3.6px;color:#555">
    <span style="color:var(--bar)">■</span> marketing &nbsp;<span style="color:var(--orange)">■</span> sg&amp;a &nbsp;<span style="color:var(--ring)">■</span> r&amp;d &nbsp;<span style="color:var(--yellow)">■</span> 1x legal
  </div>
  <svg width="120" height="120" viewBox="0 0 120 120" style="position:absolute;left:75px;top:196px" role="img" aria-label="Donut chart of seed capital use">
    <g transform="rotate(-90 60 60)" fill="none" stroke-width="20">
      <circle cx="60" cy="60" r="40" stroke="var(--bar)" stroke-dasharray="30.16 251.33" stroke-dashoffset="0"/>
      <circle cx="60" cy="60" r="40" stroke="var(--orange)" stroke-dasharray="52.78 251.33" stroke-dashoffset="-30.16"/>
      <circle cx="60" cy="60" r="40" stroke="var(--ring)" stroke-dasharray="150.8 251.33" stroke-dashoffset="-82.94"/>
      <circle cx="60" cy="60" r="40" stroke="var(--yellow)" stroke-dasharray="17.59 251.33" stroke-dashoffset="-233.74"/>
    </g>
    <g font-family="Open Sans, sans-serif" font-size="6" fill="#fff" text-anchor="middle">
      <text x="72" y="24">marketing</text><text x="72" y="31">12%</text>
      <text x="101" y="58">sg&amp;a</text><text x="101" y="65">21%</text>
      <text x="24" y="92">r&amp;d</text><text x="24" y="99">60%</text>
      <text x="46" y="23">1x legal</text><text x="46" y="30">7%</text>
    </g>
  </svg>
  <div class="foot-rule"></div><div class="foot-logo"><i></i>NOVALINK</div><div class="foot-num">5</div>
</section>

<!-- 7 Bullets -->
<section class="page c3 r2">
  <div class="head-bar"></div><div class="head-title">Headline Here</div>
  <div class="p" style="left:27px;top:44px;width:212px">In the last two weeks of January 2014 we conducted high level conversations both with your staff and your technology partner Paxwell. As a result of those conversations we've been able to gather the following high level goals for your project:</div>
  <div class="h" style="left:27px;top:71px;width:212px;font-size:6.1px;line-height:7.6px;font-weight:400;color:#666">Cloudforge must be in place to support Tidemark at launch and as the program evolves</div>
  <div class="p" style="left:27px;top:90px;width:212px;color:var(--blue);font-weight:600">The most critical aspect of this implementation both in terms of time sensitivity as well as functionality is centered around the support for the Tidemark project. Our current understanding of this project and how it relates to Cloudforge is as follows:</div>
  <div class="bl" style="top:116px"><span class="sq">■</span> <span class="black">Tidemark will be comprised of a series of websites focused on organizing institutions and individuals within six specific community sectors with the goal of increased institutional and public support to help the region become better prepared to minimize the risks and maximize opportunities of changing climate.</span><br>
  <span class="sq">■</span> <span class="black">The primary goals of the CRM application are:</span><br>
  ▸ capture information of individuals and organizations (along with their respective roles)<br>
  ▸ track their progress on their site specific to-do lists and site interactions<br>
  ▸ allow greenHorizon to push out next steps (ideally in an automated style) related to their to do list progress and online interactions<br>
  ▸ infuse greenHorizon's online and offline marketing program with useful segmentation information<br>
  ▸ natively integrate with both the Tidemark family of sites as well as greenHorizon's email service provider of choice<br>
  <span class="sq">■</span> <span class="black">The data architecture must be well defined but flexible to support the core needs of the sites at launch as well as anticipated needs in the future.</span><br>
  ▸ For instance, the faith based site may collect a "denomination" field, while other sites may not collect that field.<br>
  ▸ Future interactions outside of the to-do list may become necessary to track and greenHorizon will need a systemic way to capture those interactions, be able to segment them and potentially provide automated marketing around those similar to the to-do list<br>
  <span class="sq">■</span> <span class="black">The information collected from the Tidemark sites must be combined with current information held within greenHorizon and provide a holistic view of institutions and individuals.</span></div>
  <div class="foot-rule"></div><div class="foot-logo"><i></i>NOVALINK</div><div class="foot-num">5</div>
</section>

<!-- 8 Bar chart -->
<section class="page c4 r2">
  <div class="head-bar"></div><div class="head-title">Headline Here</div>
  <svg width="215" height="110" viewBox="0 0 215 110" style="position:absolute;left:24px;top:58px" role="img" aria-label="Monthly bar chart">
    <g fill="var(--bar)">
      <rect x="2" y="33" width="12" height="65"/><rect x="18" y="19" width="12" height="79"/><rect x="34" y="46" width="12" height="52"/>
      <rect x="50" y="69" width="12" height="29"/><rect x="66" y="92" width="12" height="6"/><rect x="82" y="71" width="12" height="27"/>
      <rect x="98" y="87" width="12" height="11"/><rect x="114" y="73" width="12" height="25"/><rect x="130" y="68" width="12" height="30"/>
      <rect x="146" y="39" width="12" height="59"/><rect x="162" y="28" width="12" height="70"/><rect x="178" y="12" width="12" height="86"/>
    </g>
    <line x1="0" y1="98" x2="194" y2="98" stroke="#bbb" stroke-width=".5"/>
    <g font-family="Open Sans, sans-serif" font-size="3.6" fill="#555" text-anchor="middle">
      <text x="8" y="30">120</text><text x="24" y="16">145</text><text x="40" y="43">96</text><text x="56" y="66">53</text>
      <text x="72" y="89">11</text><text x="88" y="68">50.5</text><text x="104" y="84">20.9</text><text x="120" y="70">46</text>
      <text x="136" y="65">55</text><text x="152" y="36">109</text><text x="168" y="25">129</text><text x="184" y="9">159</text>
      <text x="8" y="104">Jan</text><text x="24" y="104">Febr</text><text x="40" y="104">March</text><text x="56" y="104">April</text>
      <text x="72" y="104">May</text><text x="88" y="104">Jun</text><text x="104" y="104">July</text><text x="120" y="104">Aug</text>
      <text x="136" y="104">Sep</text><text x="152" y="104">Oct</text><text x="168" y="104">Nov</text><text x="184" y="104">Dec</text>
    </g>
  </svg>
  <div class="p em" style="left:27px;top:178px;font-size:4.6px">Blockchain software license or Token-as-a-License (TaaL)</div>
  <div class="p" style="left:27px;top:186px;width:212px">It is possible to create tokens on blockchain that represent software licenses, also known as Token-as-a-Licence (TaaL). Tallyo creates TaaL by using the Brindle official wallet which interacts with the Brindle blockchain. Upon purchase of TaaL, the token holder is free to transfer or sell TaaL using secondary market that is built directly over the blockchain, in our case, the Brindle marketplace. Tallyo checks the validity of a token against the blockchain ensuring that token holders have access to the software. TaaL make distribution and securisation of software licenses easier for software developers. It also makes the management and resale of software license easier for software owners. All in all, TaaL has a higher value as a normal software license.</div>
  <div class="h h2" style="left:27px;top:257px">Pre-ICO Token sale</div>
  <div class="p" style="left:27px;top:266px;width:212px">To realize this innovative vision, Tallyo is launching a pre-ICO in form of a token sale on Brindle blockchain. 20,000,000 tokens are available to purchase for the price of CHF 0.10 each during a 30-day period to be announced. Tokens represent Tallyo lifelong software licenses and by purchasing enough tokens, holders gain access to Tallyo software. 15,000 tokens give access to Tallyo invoicing or accounting. 20,000 tokens give access to both Tallyo accounting and invoicing. Future customers will still have the opportunity to buy directly yearly or monthly subscriptions to have access to Tallyo.</div>
  <div class="foot-rule"></div><div class="foot-logo"><i></i>NOVALINK</div><div class="foot-num">5</div>
</section>

<!-- 9 Photos left -->
<section class="page c1 r3">
  <div class="head-bar"></div><div class="head-title">Headline Here</div>
  <div class="photo" role="img" aria-label="Photo of a hand sketching a business diagram" style="left:27px;top:46px;width:93px;height:134px;background:linear-gradient(135deg,#2a3f6e,#9aa7c0 60%,#dfe3ec)"></div>
  <div class="photo" role="img" aria-label="Photo of a businessman reviewing documents" style="left:27px;top:203px;width:93px;height:117px;background:linear-gradient(160deg,#c9ccd2,#6b7482 55%,#2b303a)"></div>
  <div class="p lead" style="left:133px;top:45px;width:106px;font-size:5.9px;line-height:6.6px">Tallyo's mission is to help and support the self-employed and small business owners with their administrative tasks so they can focus on what matters – their business.</div>
  <div class="p" style="left:133px;top:96px;width:106px;line-height:7px">Administrative tasks are cumbersome, time-consuming and often prevent small owners from focusing their time and energy on their business and their customers. They can also be extremely stressful and nerve-wracking for those attempting these tasks for the first time.</div>
  <div class="p" style="left:133px;top:145px;width:106px;line-height:7px">At Tallyo, we envisage accounting for the self-employed and small business owners as being <span class="link">automated and decentralized</span></div>
  <div class="p" style="left:133px;top:172px;width:106px;line-height:7px">Accounting can and should be done automatically. By connecting to all sources of accounting data such as bank accounts, payment systems, e-commerce websites, and invoicing systems, Tallyo AI automatically completes these tasks, which would take hours to do manually. Bookings are created automatically and fully completed. Financial statements are available within a couple of clicks, and after analysing your data, Tallyo AI will offer you tips to improve your financial stability.</div>
  <div class="p" style="left:133px;top:256px;width:106px;line-height:7px">What may seem like a pipedream to the millions of self-employed who struggle with</div>
  <div class="h" style="left:133px;top:273px;font-size:6.8px">The Tallyo model</div>
  <div class="p" style="left:133px;top:282px;width:106px;line-height:7px">Tallyo is based on an innovative license model that uses Token-as-a-License (TaaL). The token represents lifelong software license for Tallyo solutions. The Pre-ICO token sales will enable Tallyo to complete its development of Tallyo AI to deliver fully automatic bookkeeping.</div>
  <div class="foot-rule"></div><div class="foot-logo"><i></i>NOVALINK</div><div class="foot-num">5</div>
</section>

<!-- 10 Wide photo -->
<section class="page c2 r3">
  <div class="head-bar"></div><div class="head-title">Headline Here</div>
  <div class="photo" role="img" aria-label="Photo of city traffic light trails at night" style="left:29px;top:46px;width:213px;height:90px;background:linear-gradient(160deg,#4a3a2a,#d08a2c 45%,#f4c873 70%,#8a5a28)"></div>
  <div class="p lead" style="left:27px;top:145px;width:215px;font-size:5.7px;line-height:6.2px">Tallyo's mission is to help and support the self-employed and small business owners with</div>
  <div class="p" style="left:27px;top:161px;width:215px">Administrative tasks are cumbersome, time-consuming and often prevent small owners from focusing their time and energy on their business and their customers. They can also be extremely stressful and nerve-wracking for those attempting these tasks for the first time.</div>
  <div class="p" style="left:27px;top:185px;width:215px">At Tallyo, we envisage accounting for the self-employed and small business owners as being <span class="link">automated and decentralized</span></div>
  <svg width="213" height="70" viewBox="0 0 213 70" style="position:absolute;left:29px;top:206px">
    <g stroke="var(--rule)" stroke-width=".6"><line x1="0" y1="1" x2="213" y2="1"/><line x1="0" y1="69" x2="213" y2="69"/></g>
    <g fill="var(--table-row)"><rect x="0" y="10" width="213" height="8"/><rect x="0" y="27" width="213" height="8"/><rect x="0" y="44" width="213" height="8"/><rect x="0" y="60" width="213" height="7"/></g>
  </svg>
  <div class="p" style="left:27px;top:282px;width:215px">Tallyo is based on an innovative license model that uses Token-as-a-License (TaaL). The token represents lifelong software license for Tallyo solutions. The Pre-ICO token sales will enable Tallyo to complete its development of Tallyo AI to deliver fully automatic bookkeeping.</div>
  <div class="p" style="left:27px;top:307px;width:215px">with leading edge business data access to ensure you have the best available data at your fingertips.</div>
  <div class="foot-rule"></div><div class="foot-logo"><i></i>NOVALINK</div><div class="foot-num">5</div>
</section>

<!-- 11 Solution text -->
<section class="page c3 r3">
  <div class="head-bar"></div><div class="head-title">Headline Here</div>
  <div class="h h2" style="left:27px;top:42px">Solution</div>
  <div class="p em" style="left:27px;top:52px;font-size:4.6px">AI automated accounting</div>
  <div class="p" style="left:27px;top:60px;width:212px">Tallyo builds automation in stages on top of its current system to reach full automation thanks to the Tallyo AI. Tallyo AI automates every manual task performed by the user. It starts by connecting to all sources of accounting data such as bank accounts, credit card, webshop or document management systems (Boxhive or Vaultly). Based on these datas, Tallyo AI creates bookings and generates financial reports. Finally, Tallyo AI features chat-like interface that allows users to communicate seamlessly with it, viewing it as a trusted advisor over time for all their accounting queries.</div>
  <div class="p em" style="left:27px;top:127px;font-size:4.6px">Blockchain software license or Token-as-a-License (TaaL)</div>
  <div class="p" style="left:27px;top:135px;width:212px">It is possible to create tokens on blockchain that represent software licenses, also known as Token-as-a-Licence (TaaL). Tallyo creates TaaL by using the Brindle official wallet which interacts with the Brindle blockchain. Upon purchase of TaaL, the token holder is free to transfer or sell TaaL using secondary market that is built directly over the blockchain, in our case, the Brindle marketplace. Tallyo checks the validity of a token against the blockchain ensuring that token holders have access to the software. TaaL make distribution and securisation of software licenses easier for software developers. It also makes the management and resale of software license easier for software owners. All in all, TaaL has a higher value as a normal software license.</div>
  <div class="h h2" style="left:27px;top:206px">Pre-ICO Token sale</div>
  <div class="p" style="left:27px;top:215px;width:212px">To realize this innovative vision, Tallyo is launching a pre-ICO in form of a token sale on Brindle blockchain. 20,000,000 tokens are available to purchase for the price of CHF 0.10 each during a 30-day period to be announced. Tokens represent Tallyo lifelong software licenses and by purchasing enough tokens, holders gain access to Tallyo software. 15,000 tokens give access to Tallyo invoicing or accounting. 20,000 tokens give access to both Tallyo accounting and invoicing. Future customers will still have the opportunity to buy directly yearly or monthly subscriptions to have access to Tallyo.</div>
  <div class="h h2" style="left:27px;top:277px">Future plans</div>
  <div class="p" style="left:27px;top:286px;width:212px">A future ICO is planned between 18 and 24 months after the pre-ICO token sale. This offering will support the development of Tallyo into a fully decentralized, privacy-focused ecosystem of applications. The new model will reward each participant so that a new world with zero administrative tasks becomes reality.</div>
  <div class="foot-rule"></div><div class="foot-logo"><i></i>NOVALINK</div><div class="foot-num">5</div>
</section>

<!-- 12 Back cover -->
<section class="page c4 r3 back">
  <div class="back-logo"><div class="name"><i></i>NOVALINK</div><div class="tag">NETWORK &amp; COMMUNICATIONS SOLUTIONS</div></div>
  <div class="contact">
    <span><svg width="4" height="4" viewBox="0 0 10 10"><circle cx="5" cy="5" r="5" fill="#fff"/><path d="M3 2.5 L4.3 2.5 L4.8 4 L4 4.6 C4.4 5.5 4.8 5.9 5.6 6.2 L6.2 5.4 L7.6 6 L7.6 7.2 C5 7.5 2.6 5 3 2.5 Z" fill="var(--navy)"/></svg>000-555-0142 Ext 210</span>
    <span><svg width="4" height="4" viewBox="0 0 10 10"><circle cx="5" cy="5" r="5" fill="#fff"/><rect x="2.5" y="3.2" width="5" height="3.6" fill="none" stroke="var(--navy)" stroke-width=".8"/><path d="M2.5 3.2 L5 5.2 L7.5 3.2" fill="none" stroke="var(--navy)" stroke-width=".8"/></svg>hello@novalink.example</span>
    <span><svg width="4" height="4" viewBox="0 0 10 10"><circle cx="5" cy="5" r="5" fill="#fff"/><circle cx="5" cy="5" r="2.6" fill="none" stroke="var(--navy)" stroke-width=".8"/></svg>www.novalink.example</span><br>
    12 Harbour Lane, Quarry Bay VIC 3000
  </div>
</section>

</body>
</html>
```